依頼詳細
■ 依頼詳細

子育て支援に関する事業所に配布したり、公共施設においていただいたり、保育園に訪問された方に配布したりする事を考えています。
保育園らしい温かみがあり、平積みや壁面へさしていただいても目につくようなデザインのものが好ましいです。

記載項目

添付の原稿の内容で作成をお願いします。

サイズ
A4
ページ数
片面
希望イメージ
シンプル 複雑
単色 カラフル
暗い 明るい
日常 高級
遊び心 厳粛
未来的 伝統的
女性的 男性的
希望する色
納品ファイル
• 高解像度JPG (.jpg)
• イラストレーター形式 (.ai)
• PNG形式 (.png)
補足説明
■ 補足説明

今後も同様のイベントを1回/月開催する予定があるので、日付や配布物の部分をマイナー修正できる方法も合わせて検討していただけるとありがたいです。
配布する食糧の写真を添付しました。「写真」と記載されている欄にお願いします。
写真に
「内容は毎月変わります」と一言追記をお願いします。

また、地図については、手持ちの地図がないので、作成をお願いしたいと思います。

よろしくお願い致します。
■ 選んだ理由

フードパントリーということで、物品を参加者に手渡しする、という部分が、イラストを用いて分かりやすく表現されていたので、採用させていただきました。
また、イベントが間近になっており、急いでいたこともあり、早めに対応していただいた点もよかったです。

■ 提案者全員のお礼・コメント

素敵なご提案をたくさんいただきまして、ありがとうございました。
一つを選ぶのはとても難しく、法人内でも好みが分かれて、どれも素敵で迷いました。
また、こちらの質問にもご丁寧に対応していただいた方もいらっしゃいました。
素早く反応してくださり、ありがとうございました。

```html
<!DOCTYPE html>
<html lang="ja">
<head>
<meta charset="utf-8">
<title>保育園でフードパントリー開催</title>
<link rel="stylesheet" href="https://fonts.googleapis.com/css2?family=M+PLUS+Rounded+1c:wght@500;700;800;900&family=Zen+Maru+Gothic:wght@500;700&display=swap">
<style>
:root{
  --cream:#fdf5d6;
  --green:#2f9a5a;
  --green-dark:#1f6e3f;
  --green-pale:#e3f2e3;
  --orange:#ef8a1f;
  --orange-pale:#fde7cc;
  --pink:#ef7f9a;
  --pink-pale:#fde3ea;
  --ink:#3b3027;
  --white:#ffffff;
}
*{box-sizing:border-box;margin:0;padding:0}
html,body{width:846px;height:1200px;overflow:hidden;background:var(--white)}
body{font-family:"M PLUS Rounded 1c",sans-serif;color:var(--ink)}
.flyer{position:relative;width:846px;height:1200px;background:var(--cream);overflow:hidden}
.abs{position:absolute}
.brand-top{left:26px;top:22px;display:flex;align-items:center;gap:8px;font-weight:800;font-size:15px;color:var(--green)}
.dot{width:30px;height:30px;border-radius:50%;background:var(--green)}
.ribbon{left:213px;top:34px;width:420px;height:50px;background:var(--green);color:var(--white);border-radius:25px;font-size:26px;font-weight:800;text-align:center;line-height:50px}
.lead{left:0;width:846px;top:92px;text-align:center;font-size:70px;font-weight:900;color:var(--green-dark);letter-spacing:4px}
.title-pill{left:70px;top:190px;width:600px;height:110px;background:var(--green);border-radius:55px;color:var(--white);font-size:76px;font-weight:900;text-align:center;line-height:108px;letter-spacing:2px}
.kaisai{left:652px;top:182px;width:150px;height:150px;border-radius:50%;background:var(--white);border:6px solid var(--orange);color:var(--orange);font-size:58px;font-weight:900;text-align:center;line-height:136px}
.first{left:40px;top:330px;width:104px;height:104px;border-radius:50%;background:var(--orange);color:var(--white);text-align:center;font-weight:800;font-size:18px;line-height:1.1;padding-top:20px}
.first b{font-size:40px;font-weight:900}
.date{left:160px;top:326px;font-size:50px;font-weight:900;color:var(--ink)}
.date .dow{display:inline-block;width:50px;height:50px;border-radius:50%;background:var(--green);color:var(--white);font-size:30px;text-align:center;line-height:50px;vertical-align:8px}
.venue{left:160px;top:398px;font-size:22px;font-weight:800}
.venue-addr{left:500px;top:400px;font-size:11px;line-height:1.4;font-weight:500}
.panel{top:450px;height:430px;background:var(--white);border-radius:22px;border:5px solid}
.panel.give{left:34px;width:384px;border-color:var(--orange)}
.panel.target{left:430px;width:382px;border-color:var(--pink)}
.tab{position:absolute;left:16px;top:-4px;width:92px;height:92px;border-radius:50%;color:var(--white);font-size:22px;font-weight:900;text-align:center;line-height:88px}
.give .tab{background:var(--orange)}
.target .tab{background:var(--pink)}
.panel h2{position:absolute;left:112px;right:10px;top:18px;font-size:27px;font-weight:900;line-height:1.3;text-align:center}
.photo{position:absolute;left:16px;top:112px;width:342px;height:220px;border-radius:12px;background:linear-gradient(135deg,#e9c08a,#c98a55 45%,#f3dfb8)}
.badge-val{position:absolute;left:24px;top:120px;width:70px;height:70px;border-radius:50%;background:var(--white);color:var(--orange);font-size:13px;font-weight:800;text-align:center;line-height:70px}
.monthly{position:absolute;right:24px;top:300px;background:var(--white);color:var(--orange);font-size:13px;font-weight:800;padding:3px 10px;border-radius:12px}
.medical{position:absolute;left:16px;top:344px;width:342px;font-size:14px;font-weight:700;line-height:1.5}
.medical span{background:var(--orange-pale);color:var(--orange);padding:1px 8px;border-radius:8px;margin-right:6px}
.welcome{position:absolute;left:40px;top:110px;width:292px;height:40px;background:var(--pink-pale);color:var(--pink);border-radius:20px;font-size:21px;font-weight:900;text-align:center;line-height:40px}
.illus{position:absolute;left:40px;top:162px;width:292px;height:130px;border-radius:14px;background:linear-gradient(180deg,#fff2d6,#fbd9c4)}
.playroom{position:absolute;left:20px;top:306px;width:332px;height:100px;border-radius:16px;background:var(--green-pale);border:3px solid var(--green);color:var(--green-dark);font-size:26px;font-weight:900;text-align:center;line-height:1.3;padding-top:10px}
.playroom small{display:block;font-size:12px;font-weight:700;color:var(--ink)}
.notes{left:40px;top:894px;width:766px;font-family:"Zen Maru Gothic",sans-serif;font-size:14px;font-weight:700;line-height:1.65;display:grid;grid-template-columns:1fr 1fr;column-gap:20px}
.footer{left:0;top:978px;width:846px;height:222px;background:var(--white);border-top:6px solid var(--green)}
.org{left:34px;top:1000px;display:flex;align-items:center;gap:12px}
.org .dot{width:54px;height:54px}
.org-name{font-weight:800;color:var(--green-dark)}
.org-name small{display:block;font-size:13px;font-weight:700;color:var(--ink)}
.org-name span{font-size:30px}
.tel{left:34px;top:1070px;font-size:40px;font-weight:900;color:var(--green-dark);display:flex;align-items:center;gap:8px}
.contact{left:34px;top:1124px;font-size:14px;font-weight:700;line-height:1.5}
.map{left:560px;top:996px;width:250px;height:150px;background:var(--green-pale);border:2px solid var(--green);border-radius:10px}
.foot-note{left:34px;top:1166px;width:776px;font-size:10px;line-height:1.4;color:#6b5e52}
</style>
</head>
<body>
<div class="flyer">
  <div class="abs brand-top"><span class="dot"></span>ひだまりのもり保育園</div>
  <div class="abs ribbon">子育て世帯を応援します！</div>
  <div class="abs lead">保育園で</div>
  <div class="abs title-pill">フードパントリー</div>
  <div class="abs kaisai">開催</div>

  <div class="abs first">先着<br><b>30</b>世帯</div>
  <div class="abs date">2023年9月9日<span class="dow">土</span> 11:00～12:00</div>
  <div class="abs venue">【場所】ひだまりのもり保育園</div>
  <div class="abs venue-addr">神奈川県横浜市中区みどり町1丁目2-3<br>ひだまりビル1階</div>

  <section class="abs panel give">
    <div class="tab">配布物</div>
    <h2>食料・生活用品<br>医療グッズ無料配布</h2>
    <div class="photo" role="img" aria-label="配布する食料や日用品をまとめて並べた写真"></div>
    <div class="badge-val">1万円相当</div>
    <div class="monthly">内容は毎月変わります</div>
    <p class="medical"><span>医療グッズ</span>とろみ剤／吸引用品／テープ など</p>
  </section>

  <section class="abs panel target">
    <div class="tab">対象</div>
    <h2>18歳以下の<br>お子様がいる世帯</h2>
    <div class="welcome">プレパパ、プレママも大歓迎</div>
    <div class="illus" role="img" aria-label="保育士が家族に食料の袋を手渡しするイラスト"></div>
    <div class="playroom">保育園にて<br>遊び場開放をします<small>（未就学児対象・兄弟児は小学生まで）</small></div>
  </section>

  <div class="abs notes">
    <p>※物品は1世帯1セットです</p>
    <p>※荷物が重くなりますので、大きめの袋をお持ちください</p>
    <p>※受付にて名前・世帯人数・連絡先をご記入ください</p>
    <p>※食品はアレルギー対応をしていません</p>
  </div>

  <div class="abs footer"></div>
  <div class="abs org">
    <span class="dot"></span>
    <div class="org-name"><small>企業主導型保育事業</small><span>ひだまりのもり保育園</span></div>
  </div>
  <div class="abs tel">
    <svg width="36" height="36" viewBox="0 0 24 24" aria-hidden="true"><path fill="#1f6e3f" d="M6.6 10.8a15.1 15.1 0 0 0 6.6 6.6l2.2-2.2a1 1 0 0 1 1-.25 11.4 11.4 0 0 0 3.6.57 1 1 0 0 1 1 1V20a1 1 0 0 1-1 1A17 17 0 0 1 3 4a1 1 0 0 1 1-1h3.5a1 1 0 0 1 1 1c0 1.25.2 2.45.57 3.57a1 1 0 0 1-.25 1z"/></svg>
    TEL 045-000-1234
  </div>
  <div class="abs contact">神奈川県横浜市中区みどり町1丁目2-3 ひだまりビル1階<br>MAIL：info@hidamari-mori.jp</div>
  <div class="abs map" role="img" aria-label="保育園周辺の案内地図"></div>
  <p class="abs foot-note">NPO法人ひだまりは、地域の子育て世帯を支える活動を行っています。皆さまからのご寄付・ご協力をお待ちしております。</p>
</div>
</body>
</html>
```